Flyer für IT-Firma
Zielgruppe
Wir sind eine IT-Firma, die sich unter anderem auf IT-Netzwerke spezialisiert hat. Wir verkaufen Netzwerklösungen, aber auch Produkte im Bereich IT Netzwerk, IT Security, WLAN, Cloud-Lösungen, etc. und Services. Unsere Zielgruppen für diesen Bereich sind kleinere bis Mittlere Unternehmen aber auch öffentliche Verwaltungen, Schulen, Spitäler etc. die ihre IT Netzwerke verbessern möchten und sich absichern möchten für den Fall von WLAN Ausfall oder Datenverlust. Diese Zielgruppen kennen uns womöglich noch nicht oder haben in einem anderen Projekt mit uns zusammengearbeitet. Der Flyer soll sie also von uns und dem Produkt überzeugen.
Aufgabenstellung
Der Flyer soll 2-Seitig oder 4-Seitig sein. Er soll als Vorlage für die Präsentation verschiedenster Produkte dienen. Ziel ist es einen Flyer zu haben im einheitlichen Design, den wir beliebig mit Fotos und Text abfüllen können. So dass wir unsere Produkte und Dienstleistungen im einheitlichen Design vorstellen können. Der Flyer soll folgende Elemente beinhalten:
Seite 1 eher oberflächlich das Produkt vorstellen
- Logo
- Einleitung zum Unternehmen und oder Produkt
- 1-2 Platzhalter für Bilder
- Weiterer Text für Produktbeschreibung
Seite 2 detaillierte Informationen:
- technische Daten (allenfalls in Listenform)
- Weitere Detailinformationen
- Preise
- Kontakt
Vorzugsweise Format A4 damit man auch daraus einfach ein PDF generieren kann und per Mail versenden kann. Vorschläge für andere Formate sind willkommen.

```html
<!DOCTYPE html>
<html lang="de">
<head>
<meta charset="utf-8">
<title>Netvale Solutions – Produktflyer</title>
<link rel="stylesheet" href="https://fonts.googleapis.com/css2?family=Archivo:wght@800;900&family=Poppins:wght@400;500;600;700&display=swap">
<style>
:root{
  --teal:#136577;
  --teal-dark:#0f5a6b;
  --orange:#f6992f;
  --green:#6aae4a;
  --sky:#e3f1f9;
  --sky-mid:#c9e2ef;
  --ink:#1d1d1d;
  --grey:#4a4a4a;
  --row:#eef5f3;
  --backdrop:#b1b1b1;
  --white:#ffffff;
}
*{box-sizing:border-box;margin:0;padding:0}
html,body{width:1200px;height:1117px;overflow:hidden}
body{background:var(--backdrop);font-family:"Poppins",sans-serif;color:var(--ink);position:relative}
.page{position:absolute;top:188px;width:524px;height:740px;background:var(--white);overflow:hidden;box-shadow:0 10px 24px rgba(0,0,0,.25)}
.page--front{left:63px}
.page--back{left:613px}
.page-bg{position:absolute;inset:0;width:100%;height:100%}
.abs{position:absolute}
.brand{left:0;right:0;display:flex;justify-content:center;align-items:center;gap:8px;font-weight:500;font-size:27px;color:#3d3d3d;letter-spacing:-.5px}
.brand-mark{width:14px;height:14px;background:var(--orange)}
.page--front .brand{top:30px}
.page--back .brand{top:36px}

/* front */
.headline{left:0;right:0;text-align:center;font-family:"Archivo",sans-serif;font-weight:900;line-height:1;letter-spacing:-.5px;white-space:nowrap}
.headline--teal{top:88px;font-size:48px;color:var(--teal)}
.headline--orange{top:130px;font-size:48px;color:var(--orange)}
.tagline{top:180px;left:127px;width:270px;height:28px;border-radius:4px;background:var(--green);color:var(--white);font-weight:600;font-size:17px;display:flex;align-items:center;justify-content:center}
.intro{top:217px;left:52px;width:420px;text-align:center;font-size:9.4px;line-height:12px;color:var(--ink)}
.feature{top:272px;width:216px;height:397px;border-radius:18px;color:var(--white)}
.feature--orange{left:40px;background:var(--orange)}
.feature--green{left:268px;background:var(--green)}
.feature-photo{position:absolute;top:0;left:0;width:216px;height:188px;border-radius:18px;border:4px solid var(--white)}
.feature-photo--network{background:linear-gradient(135deg,#0d3f7a,#2a7fc8 55%,#9fc6e8)}
.feature-photo--data{background:linear-gradient(135deg,#0a1a3c,#2a3f8f 50%,#c452b8 78%,#f4c04e)}
.feature-body{position:absolute;top:203px;left:24px;right:20px}
.feature-kicker{font-size:8.5px;font-weight:600;line-height:11px}
.feature-title{font-size:16.5px;font-weight:700;line-height:20px;margin-top:1px;white-space:nowrap;letter-spacing:-.2px}
.feature-rule{width:70px;height:2px;background:var(--white);margin:4px 0 8px}
.feature-text{font-size:9.8px;line-height:11.9px}
.site{left:0;right:0;top:690px;text-align:center;color:var(--white);font-weight:700;font-size:20px;letter-spacing:5px}

/* back */
.section-title{left:0;right:0;text-align:center;color:var(--teal);font-weight:700;font-size:22px}
.specs{top:124px;left:37px;width:450px;height:230px;border:2px solid var(--green);border-radius:14px;background:var(--white);padding:8px 8px}
.specs table{width:100%;border-collapse:separate;border-spacing:0}
.specs th{background:var(--orange);color:var(--white);font-weight:600;font-size:11px;height:23px;border-left:2px solid var(--white)}
.specs th:first-child{border-left:0;border-radius:6px 0 0 0}
.specs th:last-child{border-radius:0 6px 0 0}
.specs td{font-size:9px;height:18.8px;text-align:center}
.specs td:first-child{font-weight:500}
.specs tbody tr:nth-child(even) td{background:var(--row)}
.divider{top:384px;height:2px}
.divider--green{left:0;width:90px;background:var(--green)}
.divider--orange{right:0;width:90px;background:var(--orange)}
.details{top:404px;left:52px;width:420px;text-align:center;font-size:9.4px;line-height:12.8px}
.prices-bar{top:473px;left:37px;width:450px;height:27px;border-radius:4px;background:var(--green);color:var(--white);font-weight:700;font-size:17px;display:flex;align-items:center;justify-content:center}
.price{top:507px;width:222px;height:83px;border:2px solid var(--sky-mid);border-radius:10px;background:var(--white);padding:12px 16px}
.price--a{left:36px}
.price--b{left:266px}
.price-head{display:flex;justify-content:space-between;font-weight:700;font-size:16px;line-height:20px}
.price-name{color:var(--teal)}
.price-amount{color:var(--orange)}
.price-text{font-size:8px;line-height:10.5px;margin-top:5px;color:var(--grey)}
.contact{top:646px;color:var(--white);font-weight:600;font-size:15px;line-height:24px}
.contact--left{left:68px}
.contact--right{left:289px;line-height:20px;font-weight:600}
.contact-row{display:flex;align-items:center;gap:8px}
.contact-icon{width:11px;height:11px;flex:none}
.contact-split{top:652px;left:258px;width:1px;height:64px;background:rgba(255,255,255,.35)}
</style>
</head>
<body>

<section class="page page--front">
  <svg class="page-bg" viewBox="0 0 524 740" preserveAspectRatio="none" aria-hidden="true">
    <path d="M0 245 Q262 180 524 245 V740 H0Z" fill="var(--sky)"/>
    <path d="M0 640 Q262 560 524 640 V740 H0Z" fill="var(--teal)"/>
    <path d="M0 330 C22 320 38 316 40 330 V360 C30 350 10 380 0 380Z" fill="var(--teal)"/>
    <path d="M0 430 C18 420 24 415 26 420 V450 C18 450 8 455 0 458Z" fill="var(--green)"/>
  </svg>
  <div class="abs brand"><span class="brand-mark"></span>Netvale Solutions</div>
  <h1 class="abs headline headline--teal">LOREM IPSUM</h1>
  <h1 class="abs headline headline--orange">DOLOR SITAMET</h1>
  <div class="abs tagline">Lorem ipsum dolor sit amet</div>
  <p class="abs intro">Lorem ipsum dolor sit amet, consectetur adipiscing elit, sed do eiusmod tempor incididunt ut labore et dolore magna aliqua. Ut enim ad minim veniam, quis nostrud exercitation ullamco laboris nisi ut aliquip ex ea commodo consequat.</p>

  <article class="abs feature feature--orange">
    <div class="feature-photo feature-photo--network" role="img" aria-label="Foto: Netzwerk-Switch mit Patchkabeln"></div>
    <div class="feature-body">
      <div class="feature-kicker">Lorem ipsum dolor sit amet</div>
      <div class="feature-title">Lorem ipsum dolor</div>
      <div class="feature-rule"></div>
      <p class="feature-text">Lorem ipsum dolor sit amet, consectetur adipiscing elit, sed do eiusmod tempor incididunt ut labore et dolore magna aliqua. Ut enim ad minim veniam, quis nostrud exercitation ullamco laboris nisi ut aliquip ex ea commodo consequat. Duis aute irure dolor in reprehenderit in voluptate velit esse cillum dolore eu fugiat nulla pariatur.</p>
    </div>
  </article>

  <article class="abs feature feature--green">
    <div class="feature-photo feature-photo--data" role="img" aria-label="Foto: Hände an einem Laptop mit leuchtenden Datenströmen"></div>
    <div class="feature-body">
      <div class="feature-kicker">Lorem ipsum dolor sit amet</div>
      <div class="feature-title">Lorem ipsum dolor</div>
      <div class="feature-rule"></div>
      <p class="feature-text">Lorem ipsum dolor sit amet, consectetur adipiscing elit, sed do eiusmod tempor incididunt ut labore et dolore magna aliqua. Ut enim ad minim veniam, quis nostrud exercitation ullamco laboris nisi ut aliquip ex ea commodo consequat. Duis aute irure dolor in reprehenderit in voluptate velit esse cillum dolore eu fugiat nulla pariatur.</p>
    </div>
  </article>

  <div class="abs site">www.netvale.ch</div>
</section>

<section class="page page--back">
  <svg class="page-bg" viewBox="0 0 524 740" preserveAspectRatio="none" aria-hidden="true">
    <path d="M0 85 Q262 160 524 85 V560 Q262 510 0 560Z" fill="var(--sky)"/>
    <rect x="0" y="330" width="524" height="240" fill="var(--white)"/>
    <path d="M0 600 Q262 545 524 600 V740 H0Z" fill="var(--teal)"/>
    <path d="M0 230 C14 220 30 210 36 176 V244 C26 250 10 260 0 262Z" fill="var(--teal)"/>
    <path d="M0 310 C16 300 22 290 22 272 V302 C16 310 8 312 0 316Z" fill="var(--green)"/>
  </svg>
  <div class="abs brand"><span class="brand-mark"></span>Netvale Solutions</div>
  <h2 class="abs section-title" style="top:88px">Technische Daten</h2>

  <div class="abs specs">
    <table>
      <thead><tr><th>Information</th><th>Lorem ipsum</th><th>Lorem ipsum</th><th>Lorem ipsum</th></tr></thead>
      <tbody>
        <tr><td>Lorem ipsum dolor</td><td>Lorem ipsum</td><td>Lorem ipsum</td><td>Lorem ipsum</td></tr>
        <tr><td>Lorem ipsum dolor</td><td>Lorem ipsum</td><td>Lorem ipsum</td><td>Lorem ipsum</td></tr>
        <tr><td>Lorem ipsum dolor</td><td>Lorem ipsum</td><td>Lorem ipsum</td><td>Lorem ipsum</td></tr>
        <tr><td>Lorem ipsum dolor</td><td>Lorem ipsum</td><td>Lorem ipsum</td><td>Lorem ipsum</td></tr>
        <tr><td>Lorem ipsum dolor</td><td>Lorem ipsum</td><td>Lorem ipsum</td><td>Lorem ipsum</td></tr>
        <tr><td>Lorem ipsum dolor</td><td>Lorem ipsum</td><td>Lorem ipsum</td><td>Lorem ipsum</td></tr>
        <tr><td>Lorem ipsum dolor</td><td>Lorem ipsum</td><td>Lorem ipsum</td><td>Lorem ipsum</td></tr>
        <tr><td>Lorem ipsum dolor</td><td>Lorem ipsum</td><td>Lorem ipsum</td><td>Lorem ipsum</td></tr>
        <tr><td>Lorem ipsum dolor</td><td>Lorem ipsum</td><td>Lorem ipsum</td><td>Lorem ipsum</td></tr>
        <tr><td>Lorem ipsum dolor</td><td>Lorem ipsum</td><td>Lorem ipsum</td><td>Lorem ipsum</td></tr>
      </tbody>
    </table>
  </div>

  <div class="abs divider divider--green"></div>
  <div class="abs divider divider--orange"></div>
  <h2 class="abs section-title" style="top:368px">Weitere Detailinformationen</h2>
  <p class="abs details">Lorem ipsum dolor sit amet, consectetur adipiscing elit, sed do eiusmod tempor incididunt ut labore et dolore magna aliqua. Ut enim ad minim veniam, quis nostrud exercitation ullamco laboris nisi ut aliquip ex ea commodo consequat. Duis aute irure dolor in reprehenderit in voluptate velit esse cillum dolore eu</p>

  <div class="abs prices-bar">Preise</div>
  <div class="abs price price--a">
    <div class="price-head"><span class="price-name">Lorem ipsum</span><span class="price-amount">$0.0</span></div>
    <p class="price-text">Lorem ipsum dolor sit amet, consectetur adipiscing elit, sed do eiusmod tempor incididunt ut labore et dolore magna aliqua.</p>
  </div>
  <div class="abs price price--b">
    <div class="price-head"><span class="price-name">Lorem ipsum</span><span class="price-amount">$0.0</span></div>
    <p class="price-text">Lorem ipsum dolor sit amet, consectetur adipiscing elit, sed do eiusmod tempor incididunt ut labore et dolore magna aliqua.</p>
  </div>

  <div class="abs contact contact--left">
    <div class="contact-row">
      <svg class="contact-icon" viewBox="0 0 12 12" aria-hidden="true"><circle cx="6" cy="6" r="6" fill="var(--orange)"/><path d="M3.6 3.2l1.2-.4.7 1.5-.7.5c.4.9 1 1.5 1.9 1.9l.5-.7 1.5.7-.4 1.2C5.6 8.2 3.5 6.1 3.6 3.2z" fill="var(--teal)"/></svg>
      +41 41 555 01 23</div>
    <div class="contact-row">
      <svg class="contact-icon" viewBox="0 0 12 12" aria-hidden="true"><circle cx="6" cy="6" r="6" fill="var(--orange)"/><rect x="3" y="4" width="6" height="4.2" fill="none" stroke="var(--teal)" stroke-width=".9"/><path d="M3 4l3 2.3L9 4" fill="none" stroke="var(--teal)" stroke-width=".9"/></svg>
      sales@netvale.ch</div>
    <div class="contact-row">
      <svg class="contact-icon" viewBox="0 0 12 12" aria-hidden="true"><circle cx="6" cy="6" r="6" fill="var(--orange)"/><circle cx="6" cy="6" r="3" fill="none" stroke="var(--teal)" stroke-width=".8"/><path d="M3 6h6M6 3v6" stroke="var(--teal)" stroke-width=".8"/></svg>
      www.netvale.ch</div>
  </div>
  <div class="abs contact-split"></div>
  <div class="abs contact contact--right">
    <div class="contact-row">
      <svg class="contact-icon" viewBox="0 0 12 12" aria-hidden="true" style="margin-left:-19px;margin-right:0"><path d="M6 0C3.5 0 1.8 1.8 1.8 4.1 1.8 7 6 12 6 12s4.2-5 4.2-7.9C10.2 1.8 8.5 0 6 0z" fill="var(--orange)"/><circle cx="6" cy="4.2" r="1.5" fill="var(--teal)"/></svg>
      Netvale AG</div>
    <div>Lindenweg 12</div>
    <div>6300 Zug</div>
  </div>
</section>

</body>
</html>
```